Brightpath Consulting WA Business Card

Create an interesting, eye catching and colourful two sided business card. We are a business consulting operation assisting SME's improve all areas of their business. We provide consulting services to assist SME's to create a culture of continuous improvement, making a positive difference in the business. Our tag line is Small changes, big rewards. We want to create a well recognised, innovative brand that can be continued throughout our website, social media and email correspondence.

Target Market(s)

Small to Medium Enterprise Business Owners

Industry/Entity Type

Business Consultant

Contact Information for Business Card

Name of Business: Brightpath Consulting - Small Steps Bright Gains
Dean Morrow Ph 0407358164 Lydia Morrow Ph 0409583417
Email brightpathconsultingwa@examplemail.com
Web address TBA
FaceBook page TBA

BACKSIDE OF CARD

Providing assistance with:

• Organisation & Efficiency
• Revenue generation & Marketing
• Financial Management
• Production quality & delivery
• Systems & Process documentation
• Exit Strategy

Font styles to use
Other font styles liked:
• Calibri

Colors

Designer to choose colors to be used in the design.

Requirements
Must have
• Calibri font

```html
<!DOCTYPE html>
<html lang="en">
<head>
<meta charset="utf-8">
<title>Brightpath Consulting WA – Business Card</title>
<link rel="stylesheet" href="https://fonts.googleapis.com/css2?family=Open+Sans:ital,wght@0,400;0,600;0,700;1,700&display=swap">
<style>
  :root {
    --page-bg: #e4e4e4;
    --card-white: #ffffff;
    --card-dark-a: #161616;
    --card-dark-b: #3a3a3a;
    --title-grey: #3a3a3a;
    --tag-grey: #7a7a7a;
    --brand-blue: #1a8ac6;
    --phone-grey: #e2e2e2;
    --contact-grey: #555555;
    --back-title: #cfcfcf;
    --back-tag: #8a8a8a;
    --list-text: #e0e0e0;
    --mark-colour: #1a8ac6;
  }
  * { margin: 0; padding: 0; box-sizing: border-box; }
  html, body {
    width: 1125px; height: 1200px; overflow: hidden;
    background: var(--page-bg);
    font-family: "Open Sans", Calibri, sans-serif;
  }
  .card {
    position: absolute; left: 171px; width: 826px; height: 472px;
    box-shadow: 0 2px 4px rgba(0,0,0,0.25);
  }
  .card--front { top: 106px; background: var(--card-white); }
  .card--back {
    top: 639px;
    background: linear-gradient(135deg, var(--card-dark-a) 0%, #262626 55%, var(--card-dark-b) 100%);
  }

  /* front */
  .front-header { position: absolute; top: 54px; left: 0; right: 0; text-align: center; }
  .brand-name {
    font-weight: 700; font-size: 34px; letter-spacing: 0.3px;
    color: var(--title-grey); line-height: 1;
  }
  .brand-tagline {
    margin-top: 6px; font-weight: 600; font-size: 16px;
    letter-spacing: 5px; color: var(--tag-grey); line-height: 1;
  }
  .name-band {
    position: absolute; top: 164px; left: 0; width: 100%; height: 157px;
    background: linear-gradient(90deg, var(--card-dark-a) 0%, #262626 50%, var(--card-dark-b) 100%);
  }
  .person { position: absolute; top: 47px; line-height: 1; }
  .person--left { left: 52px; }
  .person--right { right: 51px; text-align: right; }
  .person__name { font-weight: 600; font-size: 29px; color: var(--brand-blue); }
  .person__phone { margin-top: 5px; font-weight: 700; font-size: 24px; color: var(--phone-grey); }
  .band-mark {
    position: absolute; left: 368px; top: 34px; width: 90px; height: 90px;
    background: var(--mark-colour);
  }
  .contact {
    position: absolute; top: 346px; left: 0; right: 0; text-align: center;
    font-size: 17px; color: var(--contact-grey); line-height: 24.5px;
  }
  .social-square {
    display: inline-block; width: 14px; height: 14px; background: var(--contact-grey);
    vertical-align: -1px; margin-right: 4px;
  }

  /* back */
  .back-brand { position: absolute; left: 44px; width: 360px; top: 118px; text-align: center; }
  .back-mark { width: 100px; height: 100px; margin: 15px auto 22px; background: var(--mark-colour); }
  .back-brand .brand-name { font-size: 23px; color: var(--back-title); }
  .back-brand .brand-tagline { margin-top: 4px; font-size: 11.5px; letter-spacing: 3.4px; color: var(--back-tag); }
  .services { position: absolute; left: 417px; top: 134px; }
  .services__title { font-weight: 700; font-style: italic; font-size: 24px; color: #ffffff; line-height: 1.2; }
  .services__list { list-style: none; margin-top: 6px; }
  .services__list li {
    font-size: 17.5px; color: var(--list-text); line-height: 24.8px; padding-left: 22px; position: relative;
  }
  .services__list li::before {
    content: ""; position: absolute; left: 4px; top: 10px; width: 6px; height: 6px;
    border-radius: 50%; background: var(--list-text);
  }
</style>
</head>
<body>
  <section class="card card--front">
    <header class="front-header">
      <div class="brand-name">BRIGHTPATH CONSULTING</div>
      <div class="brand-tagline">SMALL STEPS BRIGHT GAINS</div>
    </header>
    <div class="name-band">
      <div class="person person--left">
        <div class="person__name">DEAN MORROW</div>
        <div class="person__phone">0407358164</div>
      </div>
      <div class="band-mark" aria-hidden="true"></div>
      <div class="person person--right">
        <div class="person__name">LYDIA MORROW</div>
        <div class="person__phone">0409583417</div>
      </div>
    </div>
    <div class="contact">
      <div><span class="social-square" aria-hidden="true"></span>brightpathconsultingwa</div>
      <div>brightpathconsultingwa@examplemail.com</div>
      <div>www.brightpathconsultingwa.com</div>
    </div>
  </section>

  <section class="card card--back">
    <div class="back-brand">
      <div class="back-mark" aria-hidden="true"></div>
      <div class="brand-name">BRIGHTPATH CONSULTING</div>
      <div class="brand-tagline">SMALL STEPS BRIGHT GAINS</div>
    </div>
    <div class="services">
      <h2 class="services__title">Providing assistance with</h2>
      <ul class="services__list">
        <li>Organisation &amp; Efficiency</li>
        <li>Revenue generation &amp; Marketing</li>
        <li>Financial Management</li>
        <li>Production quality &amp; delivery</li>
        <li>Systems &amp; Process documentation</li>
        <li>Exit Strategy</li>
      </ul>
    </div>
  </section>
</body>
</html>
```